Steadfast Helm Leadership Roundtable Circuit Promotion

I'm wanting a single page (for now) website to promote my leadership training. Content would include: basic messaging what Steadfast Helm means, invitation to join the Steadfast Helm Roundtable workshops, have me come speak to them, join me on a leadership getaway, get personal coaching, watch some video links of Rud, then referrals of people saying nice things about Rud, connect to Rud’s personal website to learn more about me. The goal of the page is to 1) get people excited to attend a workshop, hear me speak, coach them, or join me on a getaway trip, 2) educate them in how they can get in control of their own life, and 3) link to my personal site to learn more about me. This is the general idea: https://www.varekquill.com/

Target Market(s)

Business owners or self improvement enthusiasts looking to take their businesses and personal lives to the next level.

Industry/Entity Type

Business Consultant

Coding

Coded - Design and coding required

Number of Pages Required

1 page

Font styles to use
Other font styles liked:
• See uploaded logo

Colors
0392cd

Requirements
Must have
• Fonts and colors that match the logo that was uploaded. Uplifting, inspirational look and feel.
Nice to have
• Similar to: https://www.varekquill.com/ and https://dorianfelsk.com/

```html
<!DOCTYPE html>
<html lang="en">
<head>
<meta charset="utf-8">
<title>Steadfast Helm</title>
<link href="https://fonts.googleapis.com/css2?family=Cinzel:wght@400;700&family=Oswald:wght@400;500&family=Raleway:wght@400;500;600&display=swap" rel="stylesheet">
<style>
:root{
  --blue:#2fbcef;
  --blue-deep:#1a95cd;
  --ink:#2b2b2d;
  --text:#6d6d72;
  --white:#ffffff;
  --dark:#29292b;
  --line:#e6e6e6;
}
*{box-sizing:border-box;margin:0;padding:0}
html,body{width:1200px;height:4510px;overflow:hidden;background:var(--white)}
body{font-family:'Raleway',sans-serif;color:var(--text);position:relative}
.abs{position:absolute}
.serif{font-family:'Cinzel',serif}
.btn{position:absolute;display:flex;align-items:center;justify-content:center;background:var(--white);color:var(--ink);border-radius:40px;font-family:'Oswald',sans-serif;font-size:20px;letter-spacing:.3px;text-transform:uppercase;box-shadow:0 0 0 5px rgba(255,255,255,.45)}
.btn.on-dark{box-shadow:0 0 0 5px var(--blue)}
.btn.on-light{box-shadow:0 0 0 5px rgba(47,188,239,.55)}
/* hero */
.hero{position:absolute;left:0;top:0;width:1200px;height:678px;background:linear-gradient(180deg,#6d7c6a 0%,#8e968c 35%,#b2b3ae 70%,#c9c8c4 100%)}
.logo{position:absolute;left:79px;top:48px;font-family:'Cinzel',serif;color:var(--white);font-size:30px;font-weight:700;line-height:1;letter-spacing:1px}
.logo small{display:block;font-size:14px;font-weight:400;letter-spacing:9px;margin-top:6px}
.nav{position:absolute;top:72px;left:0;width:1200px;font-size:15px;color:var(--white)}
.nav span{position:absolute}
.hero-title{position:absolute;top:255px;left:0;width:1200px;text-align:center;font-family:'Oswald',sans-serif;font-size:84px;font-weight:500;color:var(--blue);letter-spacing:1px}
.hero-text{position:absolute;top:366px;left:200px;width:800px;text-align:center;color:var(--white);font-size:17px;line-height:28px}
.circle-arrow{position:absolute;width:52px;height:52px;border-radius:50%;background:var(--white)}
/* feature rows */
.row{position:absolute;left:0;width:1200px}
.panel-blue{position:absolute;left:0;top:0;width:468px;height:100%;background:var(--blue)}
.photo{position:absolute;top:0;height:100%}
.row h2{position:absolute;font-family:'Cinzel',serif;font-weight:400;color:var(--white);font-size:37px;line-height:42px}
.row p{position:absolute;color:var(--white);font-size:14px;line-height:26px}
/* testimonials */
.testi{position:absolute;left:0;top:3210px;width:1200px;height:604px;background:linear-gradient(180deg,#2a9bd2,#1d92cb)}
.join{position:absolute;left:0;top:3814px;width:1200px;height:188px;background:var(--dark)}
.foot h4{position:absolute;font-family:'Cinzel',serif;font-weight:400;color:var(--blue);font-size:20px}
.foot .txt{position:absolute;font-size:14px;line-height:26px;color:var(--text)}
</style>
</head>
<body>

<!-- Hero -->
<section class="hero" role="img" aria-label="Photo of the speaker seated at a meeting table by a bright window"></section>
<div class="logo">Steadfast Helm<small>Roundtable</small></div>
<nav class="nav">
  <span style="left:492px">Workshop</span>
  <span style="left:603px">Video</span>
  <span style="left:676px">About Me</span>
  <span style="left:785px">Coaching</span>
  <span style="left:895px">Join Me</span>
  <span style="left:993px">Resources</span>
  <svg class="abs" style="left:1101px;top:-1px" width="22" height="22" viewBox="0 0 22 22"><circle cx="9" cy="9" r="7" fill="none" stroke="#fff" stroke-width="2"/><line x1="14" y1="14" x2="20" y2="20" stroke="#fff" stroke-width="2"/></svg>
</nav>
<h1 class="hero-title">STEADFAST HELM</h1>
<p class="hero-text">Lorem ipsum dolor sit amet, consectetur adipiscing elit, sed do eiusmod tempor incididunt ut labore et dolore magna aliqua. Ut enim ad minim veniam, quis nostrud.</p>
<a class="btn on-light" style="left:512px;top:443px;width:175px;height:63px">Contact Us</a>
<div class="circle-arrow" style="left:50px;top:312px"><svg width="52" height="52"><polyline points="29,19 22,26 29,33" fill="none" stroke="#222" stroke-width="3"/></svg></div>
<div class="circle-arrow" style="left:1097px;top:312px"><svg width="52" height="52"><polyline points="23,19 30,26 23,33" fill="none" stroke="#222" stroke-width="3"/></svg></div>

<!-- About -->
<section class="row" style="top:678px;height:468px">
  <div class="panel-blue"></div>
  <div class="photo" style="left:468px;width:732px;background:linear-gradient(135deg,#3b3d42,#7c7e80 55%,#c4c2bc)" role="img" aria-label="Photo of two business people shaking hands over a desk"></div>
  <h2 style="left:79px;top:58px;width:380px">About Steadfast Helm</h2>
  <p style="left:79px;top:168px;width:360px">Lorem ipsum dolor siconsectetur adipiscing elit, sed do eiusmod tempor incididunt ut labore et dolore magna aliqua. Ut enim ad minim veniam, quis nostrud exercitation ullamco laboris nisi ut aliquip ex ea commodo consequat. Duis aute irure dolor in reprehenderit in voluptate.</p>
  <a class="btn" style="left:79px;top:343px;width:175px;height:62px">Read More</a>
</section>

<!-- Speak -->
<section class="row" style="top:1146px;height:573px">
  <div class="photo" style="left:0;width:1200px;background:linear-gradient(90deg,#7f8a5a 0%,#9a4a3e 30%,#5a4a3f 50%,#2a2b2b 75%,#1f2021 100%)" role="img" aria-label="Photo of the speaker sitting on a red tractor in a field"></div>
  <h2 style="left:608px;top:124px;width:560px">Have me come speak</h2>
  <p style="left:608px;top:184px;width:520px">Lorem ipsum dolor sit amet, consectetur adipiscing elit, sed d eiusmod tempor incididunt ut labore et dolore magna aliqua. Ut enim ad minim veniam, quis nostrud exercitation ullamco laboris nisi ut aliquip ex ea commodo consequat. Duis aute irure dolor in reprehenderit in voluptate velit esse cillum dolore eu fugiat nulla pariatur. Excepteur sint occaecat cupidatat non proident, sunt in culpa qui officia deserunt mollit anim id est laborum.</p>
  <a class="btn on-dark" style="left:608px;top:396px;width:175px;height:62px">Read More</a>
</section>

<!-- Coaching -->
<section class="row" style="top:1719px;height:469px">
  <div class="panel-blue"></div>
  <div class="photo" style="left:468px;width:732px;background:linear-gradient(135deg,#d9dcd8,#a9aca8 50%,#5f6166)" role="img" aria-label="Photo of three colleagues working together at a laptop"></div>
  <h2 style="left:79px;top:63px;width:380px">Get Personal Coaching</h2>
  <p style="left:79px;top:168px;width:360px">Lorem ipsum dolor siconsectetur adipiscing elit, sed do eiusmod tempor incididunt ut labore et dolore magna aliqua. Ut enim ad minim veniam, quis nostrud exercitation ullamco laboris nisi ut aliquip ex ea commodo consequat. Duis aute irure dolor in reprehenderit in voluptate.</p>
  <a class="btn" style="left:79px;top:343px;width:175px;height:62px">Read More</a>
</section>

<!-- Getaway -->
<section class="row" style="top:2188px;height:575px">
  <div class="photo" style="left:0;width:1200px;background:linear-gradient(90deg,#c9c5bf 0%,#8f8a86 30%,#4a4744 55%,#2a2724 100%)" role="img" aria-label="Photo of a smiling woman holding a tablet in an office"></div>
  <h2 style="left:608px;top:122px;width:560px">Join me on a leadership getaway</h2>
  <p style="left:608px;top:239px;width:520px">Lorem ipsum dolor sit amet, consectetur adipiscing elit, sed d eiusmod tempor incididunt ut labore et dolore magna aliqua. Ut enim ad minim veniam, quis nostrud exercitation ullamco laboris nisi ut aliquip ex ea commodo consequat. Duis aute irure dolor in reprehenderit in voluptate velit esse cillum dolore eu fugiat nulla pariatur.</p>
  <a class="btn on-dark" style="left:608px;top:396px;width:175px;height:62px">Read More</a>
</section>

<!-- Video -->
<section class="row" style="top:2763px;height:447px">
  <div class="panel-blue"></div>
  <div class="photo" style="left:468px;width:732px;background:linear-gradient(135deg,#e3e3e0,#b9b6b0 50%,#6d6a66)" role="img" aria-label="Photo of two women talking over a laptop in an office"></div>
  <svg class="abs" style="left:802px;top:199px" width="64" height="64" viewBox="0 0 64 64"><circle cx="32" cy="32" r="29" fill="none" stroke="#fff" stroke-width="4"/><polygon points="26,20 46,32 26,44" fill="#fff"/></svg>
  <h2 style="left:79px;top:61px;width:360px">Watch some video links of Rud</h2>
  <p style="left:79px;top:210px;width:360px">Lorem ipsum dolor siconsectetur adipiscing elit, sed do eiusmod tempor incididunt ut labore et dolore magna aliqua. Ut enim ad minim veniam, quis nostrud exercitation ullamco laboris.</p>
  <a class="btn" style="left:79px;top:343px;width:175px;height:62px">Watch Video</a>
</section>

<!-- Testimonials -->
<section class="testi" role="img" aria-label="Faint conference stage photo behind the testimonials">
  <h2 class="abs serif" style="left:0;top:80px;width:1200px;text-align:center;color:#fff;font-weight:400;font-size:37px;line-height:42px">People saying nice things<br>about Rud</h2>
  <div class="abs" style="left:182px;top:227px;width:834px;height:211px;border:1px solid rgba(255,255,255,.85)"></div>
  <div class="abs" style="left:569px;top:210px;width:62px;height:52px;background:#fff"><svg width="62" height="52"><text x="31" y="44" text-anchor="middle" font-family="Cinzel,serif" font-size="54" font-weight="700" fill="#1d92cb">“</text></svg></div>
  <p class="abs" style="left:250px;top:290px;width:700px;text-align:center;color:#fff;font-size:14px;line-height:26px">Lorem Ipsum is simply dummy text of the printing and typesetting industry. Lorem Ipsum has been the industry's standard dummy text ever since the 1500s, when an unknown printer took a galley of type and scrambled it to make a type specimen book.</p>
  <div class="abs" style="left:163px;top:313px;width:40px;height:40px;background:#fff"><svg width="40" height="40"><polyline points="23,14 17,20 23,26" fill="none" stroke="#1d92cb" stroke-width="2"/></svg></div>
  <div class="abs" style="left:996px;top:313px;width:40px;height:40px;background:#fff"><svg width="40" height="40"><polyline points="17,14 23,20 17,26" fill="none" stroke="#1d92cb" stroke-width="2"/></svg></div>
  <div class="abs" role="img" aria-label="Client portrait" style="left:457px;top:399px;width:78px;height:78px;border-radius:50%;background:linear-gradient(#f3efec,#d8d2cc);border:3px solid #fff"></div>
  <div class="abs" role="img" aria-label="Client portrait" style="left:549px;top:390px;width:96px;height:96px;border-radius:50%;background:linear-gradient(#eef1f4,#c8d0d8);border:4px solid #fff;box-shadow:0 0 0 4px var(--blue)"></div>
  <div class="abs" role="img" aria-label="Client portrait" style="left:664px;top:399px;width:78px;height:78px;border-radius:50%;background:linear-gradient(#f3f1ee,#d4cfc9);border:3px solid #fff"></div>
  <div class="abs" style="left:0;top:510px;width:1200px;text-align:center;color:#fff;font-family:'Oswald',sans-serif;font-size:19px">- Client Name</div>
</section>

<!-- Join band -->
<section class="join">
  <h2 class="abs serif" style="left:79px;top:46px;color:var(--blue);font-weight:400;font-size:37px">Join the Steadfast Helm</h2>
  <p class="abs" style="left:79px;top:104px;width:760px;color:#fff;font-size:14px;line-height:26px">Lorem Ipsum is simply dummy text of the printing and typesetting industry. Lorem Ipsum has been the industry's standard dummy text ever since the 1500s, when an unknown printer.</p>
  <a class="btn on-dark" style="left:946px;top:49px;width:175px;height:61px">Join Now</a>
</section>

<!-- Footer -->
<footer class="foot">
  <div class="abs serif" style="left:79px;top:4084px;color:var(--ink);font-size:30px;font-weight:700;line-height:1">Steadfast Helm<span style="display:block;font-size:14px;font-weight:400;letter-spacing:9px;margin-top:6px">Roundtable</span></div>
  <p class="txt" style="left:79px;top:4160px;width:230px">Lorem Ipsum is simply dummy text of the printing typesetting an unknown printer.</p>
  <div class="abs" style="left:78px;top:4242px;width:44px;height:44px;border-radius:50%;background:var(--blue);box-shadow:0 2px 6px rgba(0,0,0,.12)"></div>
  <div class="abs" style="left:136px;top:4242px;width:44px;height:44px;border-radius:50%;background:#fff;box-shadow:0 2px 6px rgba(0,0,0,.15)"></div>
  <div class="abs" style="left:193px;top:4242px;width:44px;height:44px;border-radius:50%;background:#fff;box-shadow:0 2px 6px rgba(0,0,0,.15)"></div>
  <div class="abs" style="left:251px;top:4242px;width:44px;height:44px;border-radius:50%;background:#fff;box-shadow:0 2px 6px rgba(0,0,0,.15)"></div>

  <h4 style="left:349px;top:4066px">Our Company</h4>
  <div class="txt" style="left:349px;top:4114px">About Corwin<br>Team<br>Careers<br>Media Hits<br>Contact<br>Support</div>

  <h4 style="left:617px;top:4066px">Get In Touch</h4>
  <svg class="abs" style="left:617px;top:4116px" width="16" height="20" viewBox="0 0 16 20"><path d="M8 1a6 6 0 0 0-6 6c0 5 6 12 6 12s6-7 6-12a6 6 0 0 0-6-6z" fill="none" stroke="#2fbcef" stroke-width="2"/><circle cx="8" cy="7" r="2" fill="#2fbcef"/></svg>
  <div class="abs serif" style="left:653px;top:4117px;color:var(--blue);font-size:14px">Steadfast Helm</div>
  <div class="txt" style="left:653px;top:4144px">123, Address, State Name<br>City, Street, Zipcode</div>
  <svg class="abs" style="left:615px;top:4220px" width="20" height="20" viewBox="0 0 20 20"><path d="M4 2l4 1 1 4-2 2a11 11 0 0 0 4 4l2-2 4 1 1 4-2 2C9 18 2 11 2 4z" fill="#2fbcef"/></svg>
  <div class="txt" style="left:653px;top:4218px">(123) 456 7890</div>
  <svg class="abs" style="left:614px;top:4270px" width="22" height="16" viewBox="0 0 22 16"><rect x="1" y="1" width="20" height="14" fill="none" stroke="#2fbcef" stroke-width="2"/><polyline points="1,1 11,9 21,1" fill="none" stroke="#2fbcef" stroke-width="2"/></svg>
  <div class="txt" style="left:653px;top:4265px">hello@steadfasthelm.com</div>

  <h4 style="left:886px;top:4066px">Newsletter</h4>
  <p class="txt" style="left:886px;top:4114px;width:240px">To receive email releases, simply provide us with your email below</p>
  <div class="abs" style="left:885px;top:4210px;width:236px;height:65px;border-radius:33px;background:#fff;box-shadow:0 2px 10px rgba(0,0,0,.12)"></div>
  <svg class="abs" style="left:900px;top:4235px" width="20" height="14" viewBox="0 0 20 14"><rect width="20" height="14" fill="#2fbcef"/><polyline points="0,0 10,8 20,0" fill="none" stroke="#fff" stroke-width="1.5"/></svg>
  <div class="abs" style="left:934px;top:4233px;font-size:13px;color:var(--text)">Your Email</div>
  <a class="btn on-light" style="left:885px;top:4289px;width:175px;height:61px">Subscribe</a>

  <div class="abs" style="left:0;top:4424px;width:1200px;height:1px;background:var(--line)"></div>
  <div class="abs" style="left:0;top:4460px;width:1200px;text-align:center;font-size:12px;color:#9a9a9e">Copyright © <span style="color:var(--ink)">Steadfast Helm</span> - 2019 . All Right Reserved</div>
</footer>

</body>
</html>
```